KELVARA Branded Wellness Pouch Design for Clinical Study Kit

Overview:
We are creating custom zippered pouches for our “KELVARA Study Fuel Kits,” which will be distributed to physicians, nurses, and research coordinators participating in a national clinical study. We need a clean, professional design for the front of the pouch that incorporates our existing KELVARA logo and the new supporting text.
Design Requirements:
Keep the existing KELVARA logo intact (we’ll upload the file).
Add the text “Study Fuel Kit” immediately following the logo, using the same or a complementary font.
Add a tagline below that reads:
Power up. Kelvara. Go again.
Use a layout that looks balanced, legible, and polished when printed on a small pouch.
Stay consistent with our brand color palette (blue from the logo)
The overall style should feel modern, wellness-driven, and professional — think premium, science-forward, and sleek.
Audience:
This kit will be given to medical professionals, so the design should feel elevated and credible (not flashy or overly playful).
Deliverables:
Vector file (AI, EPS)
It is a frosted white, zippered vinyl pouch (9 1/2 " x 8 1/4 " x 2 1/2 ")
The imprint size is (6 3/4" W x 4 1/2" H)
The imprint can only be 1-color, so in this case - we would like the color to be the dark blue (#06173c)

```html
<!DOCTYPE html>
<html lang="en">
<head>
<meta charset="utf-8">
<title>KELVARA Study Fuel Kit – Pouch Imprint</title>
<link rel="stylesheet" href="https://fonts.googleapis.com/css2?family=Barlow+Condensed:wght@600;800&family=Montserrat:wght@800&display=swap">
<style>
  :root {
    --navy: #06173c;
    --navy-tint: rgba(6, 23, 60, 0.10);
    --navy-faint: rgba(6, 23, 60, 0);
    --paper: #f3f3f5;
  }
  * { margin: 0; padding: 0; box-sizing: border-box; }
  html, body { width: 1200px; height: 1200px; overflow: hidden; }
  body { background: var(--paper); position: relative; font-family: "Barlow Condensed", sans-serif; color: var(--navy); }

  .imprint { position: absolute; inset: 0; }

  .ring-art, .orbit-art, .molecule-art {
    position: absolute; border-radius: 50%;
    background: radial-gradient(circle, var(--navy-faint) 30%, var(--navy-tint) 62%, var(--navy-faint) 72%);
  }
  .ring-art { left: 144px; top: 512px; width: 225px; height: 220px; }
  .orbit-art { left: 650px; top: 890px; width: 160px; height: 150px; }
  .molecule-art {
    left: 940px; top: 810px; width: 200px; height: 170px; border-radius: 40%;
    background: radial-gradient(ellipse, rgba(6,23,60,0.08) 0%, rgba(6,23,60,0.04) 55%, var(--navy-faint) 75%);
  }

  .brand {
    position: absolute; left: 400px; top: 580px;
    display: flex; align-items: center; gap: 18px;
  }
  .brand-mark { width: 40px; height: 40px; background: var(--navy); }
  .brand-name { font-weight: 600; font-size: 110px; line-height: 1; letter-spacing: 1px; }

  .study-line {
    position: absolute; left: 478px; top: 694px;
    font-weight: 600; font-size: 12.5px; letter-spacing: 0.2px; white-space: nowrap;
  }
  .kit-title {
    position: absolute; left: 300px; width: 720px; top: 718px; text-align: center;
    font-weight: 800; font-size: 128px; line-height: 1; letter-spacing: 0.5px; white-space: nowrap;
  }
  .tagline {
    position: absolute; left: 380px; width: 600px; top: 860px;
    font-family: "Montserrat", sans-serif; font-weight: 800; font-size: 25px;
    text-transform: uppercase; letter-spacing: 0.4px; white-space: nowrap;
    display: flex; justify-content: center; gap: 12px; align-items: center;
  }
  .tagline .dot { width: 10px; height: 10px; border-radius: 50%; background: var(--navy); }
</style>
</head>
<body>
  <main class="imprint">
    <div class="ring-art" role="img" aria-label="Concentric line rings with small node dots"></div>
    <div class="orbit-art" role="img" aria-label="Orbit rings with small nodes"></div>
    <div class="molecule-art" role="img" aria-label="Hexagon molecule cluster with lab flasks"></div>

    <div class="brand">
      <span class="brand-mark"></span>
      <span class="brand-name">KELVARA U.S.</span>
    </div>
    <p class="study-line">ORVEN Disc Randomized, Sham-Controlled, Multi-Center, Double Blind Clinical Trial</p>

    <h1 class="kit-title">STUDY FUEL KIT</h1>

    <p class="tagline">
      <span class="dot"></span><span>Power up.</span>
      <span class="dot"></span><span>Kelvara.</span>
      <span class="dot"></span><span>Go again.</span>
    </p>
  </main>
</body>
</html>
```